A Dedicated Thank You to my Dad

Proposed Dimensions: Approx. 20" x 30"

For Father's Day, I wrote a dedication to my Dad that encapsulates my gratitude for everything he does, and everything he is. His birthday is on August 3, but it is more important for me to transform this dedication into a meaningful and memorable gift than to meet any deadline. I would love an image that captures the relationship between a father and his son, accompanied by my words of thanks in some sort of font that is appropriate for the message (calligprahy? not sure about that).

I had actually posted the Thank You on Pixelmarrow as a public post, so anyone with an account can read it: https://www.pixelmarrow.example/photo.php?fbid=40872219360548813&set=a.318760942157.6650129.3908471&type=1&theater

Only the words starting with "Thank you ..." should be on the poster.

Target Market(s)

This is a personal gift for my Dad. He doesn't have the best of eyesight, so having the words in a really small font would not be particularly helpful. :-)

Requirements
Must have
• * Personable
* Warm
* Inviting
* Memorable
* Understated more favored over Loud
Should not have
• * An entire palette of colors
* Wacky colors or fonts

```html
<!DOCTYPE html>
<html lang="en">
<head>
<meta charset="utf-8">
<title>A Dedicated Thank You to my Dad</title>
<link href="https://fonts.googleapis.com/css2?family=Delius&family=Fredoka:wght@600;700&display=swap" rel="stylesheet">
<style>
  :root{
    --night:#221d1b;
    --ink:#ffffff;
    --sun:#fff3b0;
    --amber:#f2a23a;
    --ember:#b8561a;
    --umber:#3a2418;
    --frame:#3b2a22;
    --gold:#f5c04a;
    --magenta:#d81b7a;
    --orange:#e8731c;
    --green:#7cb342;
    --rose:#f4a0b8;
    --sky:#2a9fd6;
    --pink:#e8588f;
    --yellow:#f2e12a;
    --peach:#f2a07a;
    --lavender:#b79bd6;
    --red:#d42a2a;
  }
  *{margin:0;padding:0;box-sizing:border-box}
  html,body{width:799px;height:1200px;overflow:hidden;background:var(--night)}
  .poster{
    position:relative;width:799px;height:1200px;overflow:hidden;
    background:
      linear-gradient(125deg, transparent 22%, rgba(201,110,30,.55) 38%, rgba(232,140,50,.75) 46%, rgba(190,100,30,.45) 56%, transparent 72%),
      var(--night);
    font-family:"Delius",cursive;color:var(--ink);
  }
  .sunset-scene{
    position:absolute;left:0;top:0;width:799px;height:400px;
    background:
      radial-gradient(circle at 600px 30px, var(--sun) 0, #ffd35a 60px, var(--amber) 170px, var(--ember) 380px, var(--umber) 560px),
      var(--umber);
  }
  .sunset-scene::after{
    content:"";position:absolute;left:0;right:0;top:262px;bottom:0;
    background:linear-gradient(180deg, rgba(120,60,20,.55) 0, rgba(40,22,14,.9) 55px, #0e0a08 120px, var(--night) 138px);
  }
  .title{
    position:absolute;left:38px;top:98px;width:470px;
    font-family:"Fredoka",sans-serif;font-weight:700;font-size:38px;line-height:44px;
    text-align:center;color:var(--ink);
    text-shadow:2px 3px 3px rgba(0,0,0,.75);
    transform:rotate(-7deg);transform-origin:left top;
  }
  .portrait{
    position:absolute;border-radius:50%;border:9px solid var(--frame);
    box-shadow:0 0 6px rgba(0,0,0,.5);
  }
  .portrait-dad-son{
    left:10px;top:523px;width:283px;height:228px;
    background:radial-gradient(ellipse at 55% 55%, #8a7a70 0, #b7a592 45%, #6f5a4a 100%);
  }
  .portrait-parents{
    left:533px;top:860px;width:256px;height:236px;
    background:radial-gradient(ellipse at 50% 55%, #b99a7c 0, #8d6f58 45%, #4d3a2e 100%);
  }
  .thanks{
    position:absolute;font-size:12px;line-height:18px;white-space:nowrap;
    text-shadow:1px 1px 1px rgba(0,0,0,.6);
  }
  .thanks .lead{font-family:"Fredoka",sans-serif;font-weight:600;font-size:14.5px}
  .thanks.small{font-size:11px}
  .thanks.small .lead{font-size:11.5px}
  .c-gold{color:var(--gold)} .c-magenta{color:var(--magenta)} .c-orange{color:var(--orange)}
  .c-green{color:var(--green)} .c-rose{color:var(--rose)} .c-sky{color:var(--sky)}
  .c-pink{color:var(--pink)} .c-yellow{color:var(--yellow)} .c-peach{color:var(--peach)}
  .c-lavender{color:var(--lavender)} .c-red{color:var(--red)}
  .signature{
    position:absolute;left:610px;top:1138px;
    font-family:"Fredoka",sans-serif;font-weight:700;font-size:21px;
    text-shadow:1px 2px 2px rgba(0,0,0,.7);
  }
</style>
</head>
<body>
<main class="poster">
  <div class="sunset-scene" role="img" aria-label="Photo: silhouette of a father and young son walking hand in hand on a beach at sunset"></div>
  <h1 class="title">A Dedicated Thank You<br>to my Dad</h1>

  <div class="portrait portrait-dad-son" role="img" aria-label="Photo: father and grown son standing together indoors"></div>
  <div class="portrait portrait-parents" role="img" aria-label="Photo: mother hugging father from behind at home"></div>

  <p class="thanks" style="left:50px;top:336px"><span class="lead c-gold">Thank you for</span>, after the initial shock, embracing the unexpected news that you were about to have twins.</p>
  <p class="thanks" style="left:69px;top:357px"><span class="lead c-magenta">Thank you for</span> buying enough diapers to single-handedly enable Q &amp; H to make a profit.</p>
  <p class="thanks" style="left:50px;top:378px"><span class="lead c-orange">Thank you for</span> always carrying us to the car after we fell asleep, even after we were definitely old enough to walk it.</p>
  <p class="thanks" style="left:69px;top:399px"><span class="lead c-green">Thank you for</span> not telling on us when we were only pretending to nap.</p>
  <p class="thanks" style="left:50px;top:420px"><span class="lead c-rose">Thank you for</span> welcoming more people to stay with us than I can count.</p>
  <p class="thanks" style="left:69px;top:441px"><span class="lead c-sky">Thank you for</span> sitting through more showings of "Sock Hop" and "Galaxy Raiders" than any human should endure.</p>
  <p class="thanks" style="left:50px;top:463px"><span class="lead c-pink">Thank you for</span> doggedly trying to teach me that the beach is not to be feared nor cleaned.</p>
  <p class="thanks" style="left:69px;top:484px"><span class="lead c-yellow">Thank you for</span> working two jobs, for years, to make ends meet.</p>
  <p class="thanks" style="left:238px;top:506px;text-indent:-29px"><span class="lead c-green">Thank you for</span> loading us all up in the station wagon, pillows in tow, so we could watch the first<br>drive-in movie together and squint in the second.</p>
  <p class="thanks" style="left:269px;top:543px"><span class="lead c-peach">Thank you for</span>, as coach, letting me take a fake rabbit's foot onto the soccer field.</p>
  <p class="thanks" style="left:296px;top:564px;text-indent:-10px"><span class="lead c-orange">Thank you for</span> being willing to put a hit out on my guitar teacher when he beat<br>feet.</p>
  <p class="thanks" style="left:303px;top:601px"><span class="lead c-lavender">Thank you for</span> letting me sing in my room as if I were the originating artist.</p>
  <p class="thanks" style="left:305px;top:623px"><span class="lead c-green">Thank you for</span> making car trips with you, wherever we were going, fun and<br>special.</p>
  <p class="thanks" style="left:303px;top:660px"><span class="lead c-magenta">Thank you for</span> proudly and patiently taking me to my first nerd conference in<br>junior high.</p>
  <p class="thanks" style="left:252px;top:714px;text-indent:36px"><span class="lead c-yellow">Thank you for</span> putting up with the commutes you did, for decades, so we could<br>grow up amongst family in an incredible community.</p>
  <p class="thanks" style="left:228px;top:751px"><span class="lead c-red">Thank you for</span> my dry sense of humor. I cherish it.</p>
  <p class="thanks" style="left:50px;top:774px"><span class="lead c-sky">Thank you for</span> finding a way, by hook or by crook, to send three children to college at the same time, and to allow me to go<br>to the college of my dreams.</p>
  <p class="thanks" style="left:69px;top:811px"><span class="lead c-green">Thank you for</span> never giving up on trying to convince me that imperfection is not a failure.</p>
  <p class="thanks" style="left:50px;top:832px"><span class="lead c-rose">Thank you for</span> mispronouncing, I believe on purpose, pop culture references in a way that only you can.</p>
  <p class="thanks" style="left:69px;top:853px"><span class="lead c-orange">Thank you for</span> teaching me to try to find the good in everyone.</p>
  <p class="thanks small" style="left:50px;top:872px"><span class="lead c-lavender">Thank you for</span> waiting to laugh out loud with Mom until after the police left<br>when my camp friends and I apparently made too much noise.</p>
  <p class="thanks" style="left:50px;top:923px;text-indent:19px"><span class="lead c-yellow">Thank you for</span> demonstrating the fun that can be had and the<br>truths<br>that can be gleaned from philosophical and political debate.</p>
  <p class="thanks" style="left:50px;top:994px;text-indent:19px"><span class="lead c-orange">Thank you for</span> accepting me for who I am, no matter who I love, and for<br>helping me to accept myself.</p>
  <p class="thanks" style="left:50px;top:1031px;text-indent:19px"><span class="lead c-magenta">Thank you for</span> doing whatever you can to help whoever you can, whether friend,<br>family or stranger.</p>
  <p class="thanks small" style="left:50px;top:1068px"><span class="lead c-yellow">Thank you for</span> trusting me enough to let your guard sometimes to let me know how you are<br>truly doing.</p>
  <p class="thanks" style="left:50px;top:1103px;text-indent:19px"><span class="lead c-green">Thank you for</span> insisting, year after year, that time with you means more than any gift I could<br>ever purchase. That is one lesson, amongst so many, that I will pass down to our next generation.</p>

  <p class="signature">Theo</p>
</main>
</body>
</html>
```